Tech business card design

We need an amazing business card design for our new business 'Brakka' a marketing tech startup based in Eastbay, Northland. We provide an online marketplace for businesses to search and buy advertising media, connect with service providers and learn more about marketing. We wish to communicate 'cool tech', reliability and professionalism and design based around our logo.

Target Market(s)

Business Owners

Contact Information for Business Card

Name
Position
Email Address
Website
Phone Number

Font styles to use
Other font styles liked:
• Avenir & Avenir Next

Colors

Designer to choose colors to be used in the design.

```html
<!DOCTYPE html>
<html lang="en">
<head>
<meta charset="UTF-8">
<title>Brakka Business Card</title>
<link href="https://fonts.googleapis.com/css2?family=Roboto:wght@400;500;700;900&family=PT+Serif:wght@700&display=swap" rel="stylesheet">
<style>
  :root {
    --stage: #f2f2f2;
    --navy: #03053a;
    --navy-deep: #020330;
    --white: #ffffff;
    --city-grey-top: #3a3a3a;
    --city-grey-bottom: #111111;
    --city-blue-top: #1f63c8;
    --city-blue-bottom: #0b2a78;
  }
  * { margin: 0; padding: 0; box-sizing: border-box; }
  html, body { width: 1200px; height: 1200px; overflow: hidden; background: var(--stage); }
  .stage { position: relative; width: 1200px; height: 1200px; }

  .card {
    position: absolute; left: 150px; width: 902px; height: 542px;
    background: var(--navy); overflow: hidden;
    box-shadow: 0 10px 40px rgba(0,0,0,0.45);
    font-family: "Roboto", Arial, sans-serif; color: var(--white);
  }
  .card--front { top: 25px; }
  .card--back { top: 630px; }

  .card__art { position: absolute; left: 0; top: 0; width: 902px; }
  .card--front .card__art { height: 437px; }
  .card--back .card__art { height: 398px; }

  .wordmark {
    position: absolute; font-family: "Roboto", Arial, sans-serif;
    font-weight: 900; color: var(--white); letter-spacing: -1px; line-height: 1;
  }
  .card--front .wordmark { left: 0; width: 902px; top: 215px; text-align: center; font-size: 118px; }
  .card--back .wordmark { right: 52px; top: 30px; font-size: 96px; }

  .front-url {
    position: absolute; left: 0; width: 902px; top: 472px;
    text-align: center; font-size: 21px; font-weight: 700;
  }

  .person { position: absolute; left: 0; width: 902px; text-align: center; font-family: "PT Serif", Georgia, serif; font-weight: 700; }
  .person__name { top: 206px; font-size: 37px; letter-spacing: 0.5px; }
  .person__role { top: 256px; font-size: 27px; }

  .contact { position: absolute; display: flex; align-items: center; gap: 18px; font-size: 19.5px; }
  .contact__icon { width: 25px; height: 25px; background: var(--white); display: flex; align-items: center; justify-content: center; }
  .contact__icon svg { width: 15px; height: 15px; }
  .contact--email { right: 570px; top: 412px; }
  .contact--web { right: 570px; top: 458px; }
  .contact--place { right: 75px; top: 413px; }
  .contact--phone { right: 75px; top: 458px; }
</style>
</head>
<body>
<div class="stage">

  <section class="card card--front">
    <svg class="card__art" viewBox="0 0 902 437" preserveAspectRatio="none">
      <defs>
        <linearGradient id="cityGrey" x1="0" y1="0" x2="0" y2="1">
          <stop offset="0" stop-color="var(--city-grey-bottom)"/>
          <stop offset="0.5" stop-color="var(--city-grey-top)"/>
          <stop offset="1" stop-color="var(--city-grey-bottom)"/>
        </linearGradient>
      </defs>
      <rect width="902" height="437" fill="url(#cityGrey)" role="img" aria-label="Black and white night city skyline photograph"/>
      <polygon points="0,325 560,110 902,110 902,437 0,437" fill="rgba(255,255,255,0.06)"/>
      <polygon points="275,0 902,0 902,340" fill="var(--navy)"/>
    </svg>
    <div class="wordmark">Brakka</div>
    <div class="front-url">www.brakka.com</div>
  </section>

  <section class="card card--back">
    <svg class="card__art" viewBox="0 0 902 398" preserveAspectRatio="none">
      <defs>
        <linearGradient id="cityBlue" x1="0" y1="0" x2="1" y2="1">
          <stop offset="0" stop-color="var(--city-blue-top)"/>
          <stop offset="1" stop-color="var(--city-blue-bottom)"/>
        </linearGradient>
      </defs>
      <rect width="902" height="398" fill="url(#cityBlue)" role="img" aria-label="Blue-toned aerial city skyline photograph"/>
      <polygon points="115,0 234,0 902,326 902,370" fill="rgba(170,200,255,0.28)"/>
      <polygon points="234,0 902,0 902,326" fill="var(--navy)"/>
    </svg>
    <div class="wordmark">Brakka</div>
    <div class="person person__name">MANAGER NAME</div>
    <div class="person person__role">DESIGNATION</div>

    <div class="contact contact--email">
      <span>abcd@brakka.com</span>
      <span class="contact__icon"><svg viewBox="0 0 16 16"><rect x="1.5" y="3.5" width="13" height="9" fill="none" stroke="#03053a" stroke-width="1.6"/><polyline points="1.5,3.5 8,9 14.5,3.5" fill="none" stroke="#03053a" stroke-width="1.6"/></svg></span>
    </div>
    <div class="contact contact--web">
      <span>www.brakka.com</span>
      <span class="contact__icon"><svg viewBox="0 0 16 16" fill="none" stroke="#03053a" stroke-width="1.3"><circle cx="8" cy="8" r="6.5"/><ellipse cx="8" cy="8" rx="3" ry="6.5"/><line x1="1.5" y1="8" x2="14.5" y2="8"/><line x1="2.5" y1="4.8" x2="13.5" y2="4.8"/><line x1="2.5" y1="11.2" x2="13.5" y2="11.2"/></svg></span>
    </div>
    <div class="contact contact--place">
      <span>Eastbay, Northland</span>
      <span class="contact__icon"><svg viewBox="0 0 16 16"><path d="M8 2 L1.5 8 H3.5 V14 H6.8 V10 H9.2 V14 H12.5 V8 H14.5 Z" fill="#03053a"/></svg></span>
    </div>
    <div class="contact contact--phone">
      <span>0-98-765-432-1</span>
      <span class="contact__icon"><svg viewBox="0 0 16 16"><path d="M4 1.5 L6.3 4.8 L5 6.3 C5.8 8 7.8 10.1 9.7 11 L11.2 9.7 L14.5 12 L13 14.5 C7.5 14 2 8.5 1.5 3 Z" fill="#03053a"/></svg></span>
    </div>
  </section>

</div>
</body>
</html>
```